Stationary Design for Real Estate Business
Business Card, Letterhead, Envelope Design
Professional
Derek Halvorsen
Broker/Owner
418 Pembrook Lane
Mooresville, NC 28294
derek@brantleyhomesgroup.example
www.BrantleyHomesGroup.example
We need the following designed as part of this stationary package: business card, letterhead, envelopes, 9"x12" pocket folder, and fax sheets.
Adobe Illustrator file for our logo
eps file for our logo
png file for our logo

```html
<!DOCTYPE html>
<html lang="en">
<head>
<meta charset="utf-8">
<title>Brantley Homes Group — Stationery Package</title>
<link rel="stylesheet" href="https://fonts.googleapis.com/css2?family=Cinzel:wght@600&family=Lato:wght@400;700&display=swap">
<style>
  :root {
    --backdrop: #efe9df;
    --paper: #ffffff;
    --teal-deep: #1f4f68;
    --teal: #3f7f9a;
    --teal-light: #9cc3d3;
    --grey-flap: #6f747a;
    --ink: #2a3a44;
    --muted: #8a96a0;
    --shadow: rgba(40, 30, 20, 0.18);
  }
  * { box-sizing: border-box; margin: 0; padding: 0; }
  html, body { width: 1200px; height: 446px; overflow: hidden; }
  body {
    position: relative;
    background: var(--backdrop);
    font-family: "Lato", Arial, sans-serif;
    color: var(--ink);
  }
  .sheet {
    position: absolute;
    background: var(--paper);
    box-shadow: 0 2px 6px var(--shadow);
    overflow: hidden;
  }
  .sheet svg.band { position: absolute; inset: 0; width: 100%; height: 100%; }
  .label {
    position: absolute;
    font-size: 6px;
    letter-spacing: 1.2px;
    text-transform: uppercase;
    color: var(--muted);
    white-space: nowrap;
  }
  .brand {
    position: absolute;
    display: flex;
    align-items: center;
    gap: 4px;
  }
  .brand-dot {
    border-radius: 50%;
    background: var(--teal-deep);
  }
  .brand-name {
    font-family: "Cinzel", Georgia, serif;
    font-weight: 600;
    color: var(--teal-deep);
    line-height: 1;
  }
  .watermark {
    position: absolute;
    border-radius: 50%;
    background: var(--teal-light);
    opacity: 0.18;
  }
  .fine {
    position: absolute;
    font-size: 3.6px;
    line-height: 1.5;
    color: var(--muted);
    white-space: nowrap;
  }
  /* business cards */
  .card { width: 138px; height: 44px; left: 12px; }
  .card-front { top: 132px; }
  .card-back { top: 228px; }
  /* letterheads */
  .letterhead { top: 19px; width: 283px; height: 394px; }
  .letterhead-one { left: 173px; }
  .letterhead-two { left: 473px; }
  /* envelopes */
  .envelope-back { left: 806px; top: 18px; width: 370px; height: 232px; }
  .envelope-front { left: 806px; top: 290px; width: 370px; height: 136px; }
</style>
</head>
<body>

  <!-- Business cards -->
  <div class="label" style="left:12px; top:114px;">Stationery Concepts</div>

  <div class="sheet card card-front">
    <svg class="band" viewBox="0 0 138 44" preserveAspectRatio="none" aria-hidden="true">
      <rect width="138" height="44" fill="var(--teal-deep)"/>
      <path d="M0 30 Q70 18 138 26 L138 44 L0 44 Z" fill="var(--teal)"/>
    </svg>
    <div class="brand" style="left:18px; top:14px;">
      <span class="brand-dot" style="width:8px;height:8px;background:var(--paper);"></span>
      <span class="brand-name" style="font-size:9px;color:var(--paper);">Brantley</span>
    </div>
  </div>
  <div class="label" style="left:12px; top:181px;">Business Card Front</div>

  <div class="sheet card card-back">
    <svg class="band" viewBox="0 0 138 44" preserveAspectRatio="none" aria-hidden="true">
      <path d="M0 36 Q70 28 138 34 L138 44 L0 44 Z" fill="var(--teal-deep)"/>
    </svg>
    <div class="brand" style="left:18px; top:10px;">
      <span class="brand-dot" style="width:8px;height:8px;"></span>
      <span class="brand-name" style="font-size:9px;">Brantley</span>
    </div>
    <div class="fine" style="left:82px; top:9px;">Derek Halvorsen<br>Broker/Owner<br>418 Pembrook Lane<br>Mooresville, NC 28294</div>
  </div>
  <div class="label" style="left:12px; top:277px;">Business Card Back</div>

  <!-- Letterhead option 1 -->
  <div class="sheet letterhead letterhead-one">
    <svg class="band" viewBox="0 0 283 394" preserveAspectRatio="none" aria-hidden="true">
      <path d="M0 0 L22 0 Q8 200 22 394 L0 394 Z" fill="var(--teal-deep)"/>
      <path d="M22 0 Q8 200 22 394 L27 394 Q13 200 27 0 Z" fill="var(--teal-light)"/>
    </svg>
    <div class="brand" style="left:38px; top:16px;">
      <span class="brand-dot" style="width:10px;height:10px;"></span>
      <span class="brand-name" style="font-size:11px;">Brantley</span>
    </div>
    <div class="fine" style="left:170px; top:14px;">418 Pembrook Lane<br>Mooresville, NC 28294<br>derek@brantleyhomesgroup.example<br>www.BrantleyHomesGroup.example</div>
    <div class="watermark" style="left:97px; top:150px; width:90px; height:90px;"></div>
  </div>
  <div class="label" style="left:273px; top:420px;">Letterhead Option 1</div>

  <!-- Letterhead option 2 -->
  <div class="sheet letterhead letterhead-two">
    <svg class="band" viewBox="0 0 283 394" preserveAspectRatio="none" aria-hidden="true">
      <path d="M0 0 L18 0 Q4 200 18 394 L0 394 Z" fill="var(--teal-deep)"/>
      <path d="M18 0 Q4 200 18 394 L22 394 Q8 200 22 0 Z" fill="var(--teal-light)"/>
    </svg>
    <div class="watermark" style="left:97px; top:70px; width:90px; height:90px;"></div>
    <div class="brand" style="left:102px; top:166px;">
      <span class="brand-dot" style="width:10px;height:10px;opacity:.35;"></span>
      <span class="brand-name" style="font-size:11px;opacity:.35;">Brantley</span>
    </div>
    <div class="fine" style="left:40px; top:378px;">418 Pembrook Lane · Mooresville, NC 28294 · derek@brantleyhomesgroup.example · www.BrantleyHomesGroup.example</div>
  </div>
  <div class="label" style="left:573px; top:420px;">Letterhead Option 2</div>

  <!-- Envelope back -->
  <div class="sheet envelope-back">
    <svg class="band" viewBox="0 0 370 232" preserveAspectRatio="none" aria-hidden="true">
      <rect width="370" height="50" fill="var(--teal-deep)"/>
      <path d="M0 50 L370 50 L370 62 Q185 150 0 62 Z" fill="var(--grey-flap)"/>
      <path d="M0 232 L150 140 L220 140 L370 232 Z" fill="#f3f5f6"/>
      <path d="M0 110 L160 150 L0 232 Z" fill="#f7f8f9"/>
      <path d="M370 110 L210 150 L370 232 Z" fill="#f7f8f9"/>
    </svg>
    <div class="brand" style="left:163px; top:92px;">
      <span class="brand-dot" style="width:9px;height:9px;"></span>
      <span class="brand-name" style="font-size:9px;">Brantley</span>
    </div>
  </div>

  <!-- Envelope front -->
  <div class="sheet envelope-front">
    <svg class="band" viewBox="0 0 370 136" preserveAspectRatio="none" aria-hidden="true">
      <path d="M0 0 L14 0 Q6 68 14 136 L0 136 Z" fill="var(--teal-deep)"/>
    </svg>
    <div class="brand" style="left:28px; top:12px;">
      <span class="brand-dot" style="width:9px;height:9px;"></span>
      <span class="brand-name" style="font-size:10px;">Brantley</span>
    </div>
    <div class="fine" style="left:28px; top:28px;">418 Pembrook Lane<br>Mooresville, NC 28294</div>
    <div class="watermark" style="left:150px; top:20px; width:80px; height:80px;"></div>
  </div>
  <div class="label" style="left:948px; top:432px;">Envelope Option</div>

</body>
</html>
```